Affinity Card (Brochure for a Fuel Card )

We need a brochure developed for a Fuel Card our company is offering to the market. Our offer has many different elements to it and as well as the benefits of the card it has geographical spread across Australia where the card is taken and where we can offer lucrative deals . The design should show the benefits of our card and also the fact it has the ability to be used Nationally as well as locally. The final design should communicate that the card is linked to both Harrowgate and Corvane (cant use the corvane logo)
The design should have a section for the applicant to put his name and address , l have supplied an example from America but want it different
It can have up to 4 folds no issues
Below are ideas for use

Target Market(s)

Fuel Card Users in all segments

Industry/Entity Type

It Company

Requirements
Must have
• Be able to capture attention and be handed out
• We now need the use of the Corvane sites in the brochure and drop the truck top image
• Sorry about the changes

```html
<!DOCTYPE html>
<html lang="en">
<head>
<meta charset="utf-8">
<title>Harrowgate Corvane Fuel Card Brochure</title>
<link rel="stylesheet" href="https://fonts.googleapis.com/css2?family=Arimo:wght@700&family=Open+Sans:ital,wght@0,400;1,400&display=swap">
<style>
:root{
  --ink:#1a1a1a;
  --panel-blue:#4b8fce;
  --accent-red:#e2262b;
  --accent-blue:#3f86c9;
  --white:#ffffff;
  --rule:#c9a6b8;
  --photo-station:#b9c6d2;
  --photo-hands:#9fa8b0;
  --map-land:#e7e3d6;
}
*{margin:0;padding:0;box-sizing:border-box}
html,body{width:1200px;height:743px;overflow:hidden;background:var(--white)}
.brochure{position:relative;width:1200px;height:743px;font-family:"Open Sans",Arial,sans-serif;color:var(--ink)}
.panel{position:absolute;top:0;height:743px}
.panel-left{left:0;width:408px}
.panel-middle{left:408px;width:385px;background:var(--panel-blue);color:var(--white)}
.panel-right{left:793px;width:407px}
h2{font-family:"Arimo",Arial,sans-serif;font-weight:700;font-size:12.5px;letter-spacing:.1px;text-transform:uppercase}
.panel-left h2{position:absolute;left:22px}
.feature-list{list-style:none;position:absolute;left:22px;font-style:italic;font-size:11.2px;line-height:19.2px}
.station-photo{position:absolute;left:175px;top:66px;width:211px;height:188px;background:linear-gradient(180deg,#9fc0dc 0%,#c8d6e0 45%,var(--photo-station) 100%)}
.divider{position:absolute;left:22px;width:364px;border-top:1px dotted var(--rule)}
.card-list{list-style:none;position:absolute;left:22px;top:315px;width:370px;font-style:italic;font-size:11.2px;line-height:19.2px}
.map-band{position:absolute;left:0;top:395px;width:408px;height:348px}
.panel-middle h2{position:absolute;left:21px;color:var(--white);font-size:12.5px}
.lead{position:absolute;left:21px;font-size:12px;width:350px;line-height:15.5px}
.bullets{list-style:none;position:absolute;left:21px;width:345px;font-style:italic;font-size:10.4px;line-height:14px}
.bullets li{position:relative;padding-left:19px;margin-bottom:13px}
.bullets li::before{content:"";position:absolute;left:0;top:4px;width:6px;height:6px;background:var(--white)}
.security-list{top:86px}
.control-list{top:338px}
.middle-rule{position:absolute;left:21px;top:419px;width:344px;border-top:1px dotted rgba(255,255,255,.8)}
.locations{list-style:none;position:absolute;left:21px;top:471px;font-style:italic;font-size:10.4px}
.locations li{position:relative;padding-left:19px;height:22.3px}
.locations li::before{content:"";position:absolute;left:0;top:4px;width:6px;height:6px;background:var(--white)}
.hero{position:absolute;left:0;top:0;width:407px;height:420px}
.copy-block{position:absolute;left:19px;width:376px}
.copy-block h2{font-size:12.5px;margin-bottom:3px}
.copy-block p{font-size:9.2px;line-height:13.7px;text-align:justify;margin-bottom:10px}
</style>
</head>
<body>
<div class="brochure">

  <section class="panel panel-left">
    <h2 style="top:40px">Reduce Fraud Risk - Manage Your Account Online</h2>
    <ul class="feature-list" style="top:59px">
      <li>(i) Download Statements</li>
      <li>(ii) Concise fleet reporting</li>
      <li>(iii) Automatic reporting</li>
      <li>(iv) Odometer audits</li>
      <li>(v) Transaction extracts</li>
      <li>(vi) Cost centre summary</li>
      <li>(vii) Litres per 100km</li>
      <li>(viii) Active card listings</li>
      <li>(ix) Expiring fuel cards</li>
      <li>(x) Exception reports</li>
    </ul>
    <div class="station-photo" role="img" aria-label="Photo of a truck fuel station with pumps under a canopy"></div>
    <div class="divider" style="top:277px"></div>
    <h2 style="top:292px">Customised Card Management</h2>
    <ul class="card-list">
      <li>(i) Card management – order, delete, suspend and alter cards. Manage cost centres &amp; set pins</li>
      <li>(ii) Shop sales option</li>
      <li>(iii) Truck wash option</li>
    </ul>
    <svg class="map-band" viewBox="0 0 408 348" aria-hidden="false">
      <polygon points="0,2 408,100 408,112 0,12" fill="var(--accent-red)"/>
      <polygon points="0,12 408,112 408,124 0,22" fill="var(--accent-blue)"/>
      <g role="img" aria-label="Map of Victoria showing fuel card site locations">
        <defs>
          <linearGradient id="mapTone" x1="0" y1="0" x2="0" y2="1">
            <stop offset="0" stop-color="var(--map-land)"/>
            <stop offset=".7" stop-color="#e2e6d8"/>
            <stop offset="1" stop-color="#a9c6e8"/>
          </linearGradient>
        </defs>
        <polygon points="0,22 408,124 408,348 0,348" fill="url(#mapTone)"/>
      </g>
    </svg>
  </section>

  <section class="panel panel-middle">
    <h2 style="top:40px">Security</h2>
    <p class="lead" style="top:63px">We recognise that card security is a priority for all customers</p>
    <ul class="bullets security-list">
      <li>Personal Identification Number (PIN) - the preferred security measure, PINs can be used for vehicle specific cards and for those cardholders who prefer a PIN instead of a signature</li>
      <li>Signature - used in cases where the card will only be used by an individual cardholder.</li>
      <li>Odometer readings - when selected, cardholders will be prompted to supply odometer readings to the console operator at time of purchase. The use of odometer readings provides additional tracking measures for the organisation.</li>
      <li>Purchase limits - can also be nominated on individual cards and will restrict purchases by time, volume or dollars</li>
    </ul>
    <p class="lead" style="top:301px">Control /Flexibility/ Simplicity and Convenience the cornerstone of our card offer</p>
    <ul class="bullets control-list">
      <li>We let and enable you to control your cards and your business in the simplest possible way</li>
      <li>Payment terms up to 50 days from transaction</li>
    </ul>
    <div class="middle-rule"></div>
    <h2 style="top:435px;line-height:15px">24 Hour Truck Locations<br>We Have Developed For You</h2>
    <ul class="locations">
      <li>Laverton – 4-16 Quarry Lane Laverton North Victoria.</li>
      <li>Merredin – Lot 2207 Fenwick Crescent Merredin WA 6409</li>
      <li>Roma – 38 Ashdale Street Roma Qld 4462</li>
      <li>Griffith – 3-9 Tallow Avenue Griffith NSW 2687</li>
      <li>Warwick – 15 Birchley Street Warwick QLD 4375</li>
      <li>Bendigo – 214 Harlowe Road Bendigo Victoria 3558</li>
      <li>Benalla – Range View Road Benalla Victoria.</li>
      <li>Katanning – 9 Cove Street Katanning WA 6312</li>
      <li>Katherine – Cnr Ridgeway Drive and Pellam Crescent Katherine NT 0856</li>
    </ul>
  </section>

  <section class="panel panel-right">
    <svg class="hero" viewBox="0 0 407 420">
      <defs>
        <linearGradient id="handsTone" x1="0" y1="0" x2="1" y2="1">
          <stop offset="0" stop-color="#5b6168"/>
          <stop offset=".5" stop-color="var(--photo-hands)"/>
          <stop offset="1" stop-color="#cfd6dc"/>
        </linearGradient>
      </defs>
      <g role="img" aria-label="Photo of two business people shaking hands">
        <polygon points="0,0 407,0 407,395 0,318" fill="url(#handsTone)"/>
      </g>
      <polygon points="150,0 407,0 407,48" fill="var(--white)"/>
      <polygon points="150,0 175,0 407,52 407,58" fill="var(--accent-red)"/>
      <polygon points="175,0 200,0 407,48 407,52" fill="var(--accent-blue)"/>
      <polygon points="0,318 407,395 407,420 0,342" fill="var(--white)"/>
      <polygon points="0,316 407,382 407,392 0,326" fill="var(--accent-red)"/>
      <polygon points="0,326 407,392 407,398 0,332" fill="var(--accent-blue)"/>
      <polygon points="0,332 407,398 407,404 0,336" fill="#151515"/>
    </svg>
    <div class="copy-block" style="top:406px">
      <h2>Lorem Ipsum Dolor</h2>
      <p>Lorem Ipsum is simply dummy text of the printing and typesetting industry. Lorem Ipsum has been the industry's standard dummy text ever since the 1500s, when an unknown printer took a galley of type and scrambled it to make a type specimen book. It has survived not only five centuries, but also the leap into electronic typesetting, remaining essentially unchanged.</p>
      <p>Lorem Ipsum is simply dummy text of the printing and typesetting industry. Lorem Ipsum has been the industry's standard dummy text ever since the 1500s, when an unknown printer took a galley of type and scrambled it to make a type specimen book. It has survived not only five centuries, but also the leap into electronic typesetting, remaining essentially unchanged.</p>
    </div>
    <div class="copy-block" style="top:580px">
      <h2>Lorem Ipsum Dolor</h2>
      <p>Lorem Ipsum is simply dummy text of the printing and typesetting industry. Lorem Ipsum has been the industry's standard dummy text ever since the 1500s, when an unknown printer took a galley of type and scrambled it to make a type specimen book. It has survived not only five centuries, but also the leap into electronic typesetting, remaining essentially unchanged.</p>
      <p>Lorem Ipsum is simply dummy text of the printing and typesetting industry. Lorem Ipsum has been the industry's standard dummy text ever since the 1500s, when an unknown printer took a galley of type and scrambled it to make a type specimen book was there.</p>
    </div>
  </section>

</div>
</body>
</html>
```